Business Card Design

I am a realtor and i also flip houses. I am CEO and Founder of my business which is Vantrell Group LLC which is named after my great uncle who died and i was really close to. He was a wonderful friendly man so i want my business to represent him too. My business works with a lot of different people but i want mainly something to show i am a strong confidant woman who owns there own business. I have a really fun personality so i don't want anything TOO serious or manly. I want the perfect mix. My last two business cards i created are too embarrassing to hand out because they are far too girly and i deal with a lot of millionaire clients. I live out in the Palm Springs California area. I think its very important to show i am a single mom, female with her own business at only 24. I don't want to just be a female that blends in with all of the other serious people but yet i don't want to seem immature. People are telling me to stay away from pinks and purples but i don't want blues and greens because they represent men more. But i won't say no to them if there is a happy medium.

Industry/Entity Type

Realtor

Contact Information for Business Card

Vantrell Group, LLC
Corinne Haskett
27385 Sandvale Ave, C2 518
Cresta Mirada, CA 92999
760-413-6657
Corinnethaskett@mailvern.com

```html
<!DOCTYPE html>
<html lang="en">
<head>
<meta charset="utf-8">
<title>Vantrell Group, LLC — Business Card</title>
<link rel="stylesheet" href="https://fonts.googleapis.com/css2?family=Source+Sans+3:wght@400&display=swap">
<style>
  :root {
    --page: #ffffff;
    --bleed: #000000;
    --card-red: #c62d36;
    --card-red-light: #dc4b50;
    --ink-light: #fbf4ea;
    --mark-cream: #f5eedf;
  }
  html, body {
    margin: 0;
    padding: 0;
    width: 1200px;
    height: 1000px;
    overflow: hidden;
    background: var(--page);
    font-family: "Source Sans 3", "Myriad Pro", Arial, sans-serif;
  }
  .canvas {
    position: relative;
    width: 1200px;
    height: 1000px;
  }
  .card-bleed {
    position: absolute;
    left: 58px;
    top: 183px;
    width: 1085px;
    height: 635px;
    background: var(--bleed);
  }
  .card {
    position: absolute;
    left: 103px;
    top: 225px;
    width: 993px;
    height: 550px;
    background: radial-gradient(ellipse 55% 60% at 52% 52%, var(--card-red-light), var(--card-red) 100%);
    color: var(--ink-light);
  }
  .brand-dot {
    position: absolute;
    left: 440px;
    top: 68px;
    width: 110px;
    height: 110px;
    border-radius: 50%;
    background: var(--mark-cream);
  }
  .brand-name {
    position: absolute;
    left: 0;
    top: 184px;
    width: 990px;
    text-align: center;
    font-size: 52px;
    line-height: 1;
    letter-spacing: 0.8px;
    margin: 0;
    font-weight: 400;
  }
  .person {
    position: absolute;
    right: 6px;
    top: 38px;
    width: 320px;
    text-align: center;
    margin: 0;
  }
  .person-name {
    display: block;
    font-size: 38px;
    line-height: 46px;
    letter-spacing: 1.2px;
  }
  .person-title {
    display: block;
    font-size: 31px;
    line-height: 48px;
    letter-spacing: 0.6px;
  }
  .address {
    position: absolute;
    left: 42px;
    top: 350px;
    margin: 0;
    font-style: normal;
    font-size: 39px;
    line-height: 50px;
    letter-spacing: 1px;
  }
  .divider {
    position: absolute;
    left: 480px;
    top: 340px;
    width: 8px;
    height: 180px;
  }
  .contact {
    position: absolute;
    left: 508px;
    top: 370px;
    margin: 0;
    font-size: 39px;
    line-height: 50px;
    letter-spacing: 1.2px;
  }
  .contact .email {
    font-size: 35px;
    letter-spacing: 0.4px;
  }
</style>
</head>
<body>
<div class="canvas">
  <div class="card-bleed"></div>
  <section class="card">
    <div class="brand-dot"></div>
    <h1 class="brand-name">Vantrell Group, LLC</h1>

    <p class="person">
      <span class="person-name">Corinne Haskett</span>
      <span class="person-title">CEO and Founder</span>
    </p>

    <address class="address">
      27385 Sandvale Ave<br>
      C2 518 Cresta Mirada<br>
      CA 92999
    </address>

    <svg class="divider" viewBox="0 0 8 180" aria-hidden="true">
      <path d="M4 0 L5.5 90 L4 180 L2.5 90 Z" fill="var(--ink-light)"/>
    </svg>

    <p class="contact">
      <span class="phone">760-413-6657</span><br>
      <span class="email">Corinnethaskett@mailvern.com</span>
    </p>
  </section>
</div>
</body>
</html>
```